Dorsey K. Wendell Business Card

We need a business card for our company Dorsey K. Wendell Heating & Plumbing to be distributed to potential customers. It should follow the color scheme of our logo and have a modern upscale and masculine look.

The logo is attached and the info below should also be included:

5187 W. Cedar Brook Rd.
Brookvale, PA 17599

Russell T. Wendell
(717) 592-0817
russelltwendell@fernmail.net
dorseykwendell.net
PA #093148

Industry/Entity Type

Business

Contact Information for Business Card

5187 W. Cedar Brook Rd.
Brookvale, PA 17599

Russell T. Wendell
(717) 592-0817
russelltwendell@fernmail.net
dorseykwendell.net
PA #093148

Colors

Designer to choose colors to be used in the design.

Requirements
Must have
• Information above included

```html
<!DOCTYPE html>
<html lang="en">
<head>
<meta charset="utf-8">
<title>Dorsey K. Wendell Business Card</title>
<link rel="stylesheet" href="https://fonts.googleapis.com/css2?family=Open+Sans:wght@400;600;700;800&display=swap">
<style>
  :root {
    --brand-blue: #0d4f9e;
    --brand-green: #9acb3c;
    --card-white: #ffffff;
    --stage: #eceae6;
    --text-light: #ffffff;
  }
  html, body {
    margin: 0;
    padding: 0;
    width: 1200px;
    height: 755px;
    overflow: hidden;
    background: var(--stage);
    font-family: "Open Sans", Arial, sans-serif;
  }
  .canvas {
    position: relative;
    width: 1200px;
    height: 755px;
  }
  .card {
    position: absolute;
    top: 230px;
    width: 520px;
    height: 294px;
    background: var(--card-white);
    box-shadow: 0 6px 18px rgba(0,0,0,0.18);
    overflow: hidden;
  }
  .card--front { left: 60px; }
  .card--back { left: 620px; }

  /* Front */
  .front-brand {
    position: absolute;
    inset: 0;
    display: flex;
    align-items: center;
    justify-content: center;
    gap: 14px;
  }
  .brand-square {
    width: 46px;
    height: 46px;
    background: var(--brand-blue);
    flex: none;
  }
  .brand-name {
    color: var(--brand-blue);
    font-weight: 800;
    font-size: 30px;
    line-height: 1.05;
    text-transform: uppercase;
    letter-spacing: 0.5px;
    white-space: nowrap;
  }
  .brand-name span { display: block; font-size: 15px; letter-spacing: 1.2px; }

  /* Back */
  .back-shapes {
    position: absolute;
    inset: 0;
  }
  .holder-name {
    position: absolute;
    left: 16px;
    top: 30px;
    color: var(--brand-green);
    font-weight: 700;
    font-size: 17px;
    letter-spacing: 0.6px;
  }
  .contact {
    position: absolute;
    left: 16px;
    top: 155px;
    color: var(--text-light);
    font-size: 12.5px;
    line-height: 1.25;
    letter-spacing: 0.3px;
  }
  .contact p { margin: 0; }
  .contact .address { margin-bottom: 12px; }
  .contact .line { display: flex; align-items: center; gap: 5px; margin-bottom: 6px; }
  .contact .line svg { width: 11px; height: 11px; flex: none; }
  .contact .license { margin-top: 9px; }
  .back-brand {
    position: absolute;
    left: 296px;
    right: 10px;
    top: 132px;
    display: flex;
    align-items: center;
    gap: 7px;
  }
  .back-brand .brand-square { width: 24px; height: 24px; }
  .back-brand .brand-name { font-size: 14px; letter-spacing: 0.2px; }
  .back-brand .brand-name span { font-size: 8px; letter-spacing: 0.9px; }
</style>
</head>
<body>
<main class="canvas">
  <section class="card card--front" aria-label="Card front">
    <div class="front-brand">
      <div class="brand-square"></div>
      <div class="brand-name">Dorsey K. Wendell<span>Heating &amp; Plumbing</span></div>
    </div>
  </section>

  <section class="card card--back" aria-label="Card back">
    <svg class="back-shapes" viewBox="0 0 520 294" width="520" height="294" aria-hidden="true">
      <path d="M0,0 H253 C240,80 236,200 248,294 H0 Z" fill="var(--brand-blue)"/>
      <path d="M253,0 H290 C265,60 250,180 250,294 H248 C236,200 240,80 253,0 Z" fill="var(--brand-green)"/>
    </svg>

    <div class="holder-name">Russell T. Wendell</div>

    <div class="contact">
      <p class="address">5187 W. Cedar Brook Rd.<br>Brookvale, PA 17599</p>
      <p class="line">
        <svg viewBox="0 0 12 12"><circle cx="6" cy="6" r="5" fill="none" stroke="var(--brand-green)" stroke-width="1.2"/><path d="M4.2 3.4 L5.2 3.3 L5.6 4.8 L5 5.3 Q5.6 6.6 6.7 7 L7.2 6.4 L8.6 6.8 L8.6 7.8 Q6.5 8.6 4.6 6.6 Q3.4 5 4.2 3.4 Z" fill="var(--brand-green)"/></svg>
        (717) 592-0817
      </p>
      <p class="line">
        <svg viewBox="0 0 12 12"><rect x="1" y="3" width="10" height="6.5" fill="var(--brand-green)"/><path d="M1 3 L6 7 L11 3" fill="none" stroke="var(--brand-blue)" stroke-width="0.9"/></svg>
        russelltwendell@fernmail.net
      </p>
      <p class="line">
        <svg viewBox="0 0 12 12"><circle cx="6" cy="6" r="5" fill="none" stroke="var(--brand-green)" stroke-width="1"/><ellipse cx="6" cy="6" rx="2.2" ry="5" fill="none" stroke="var(--brand-green)" stroke-width="0.9"/><path d="M1 6 H11" stroke="var(--brand-green)" stroke-width="0.9"/></svg>
        www.dorseykwendell.net
      </p>
      <p class="license">PA #093148</p>
    </div>

    <div class="back-brand">
      <div class="brand-square"></div>
      <div class="brand-name">Dorsey K. Wendell<span>Heating &amp; Plumbing</span></div>
    </div>
  </section>
</main>
</body>
</html>
```